Lanternfield Dance Business Card

I'm looking for a two-sided business card design to promote my country dance busness. Cowboy hats, boots, and wood grain floor textures, are all appropriate to use.
On one side I want it to say:
Lanternfield Dance
with
Mark
Take The Challenge - Experience The Growth
210-574-2318
On the other side I want:
A place for a Head Shot
The Quote: Experience Is The Best Teacher
A two column bullet list with the following:
First column: Two Step, Waltz, Triple Two, Polka
Second column: Cha-Cha, West Coast, East Cost, NightClub
My Name: Mark Delby
My Phone Number: 210-574-2318
Please see attached drawing

```html
<!DOCTYPE html>
<html lang="en">
<head>
<meta charset="utf-8">
<title>Lanternfield Dance Business Card</title>
<link rel="stylesheet" href="https://fonts.googleapis.com/css2?family=Lobster&family=Alfa+Slab+One&family=Lora:ital@1&family=Oswald:wght@600&family=Montserrat:wght@500;600;800&display=swap">
<style>
  :root {
    --stage: #dcdcdc;
    --card: #7c4119;
    --card-deep: #6a3512;
    --ink: #3b1b07;
    --cream: #f2c993;
    --tan: #d08c52;
    --tan-light: #e6a66a;
    --leather: #8d5428;
  }
  * { box-sizing: border-box; margin: 0; padding: 0; }
  html, body { width: 1200px; height: 800px; overflow: hidden; }
  body {
    background: var(--stage);
    display: flex; flex-direction: column; align-items: center; justify-content: center;
    gap: 30px;
    color: var(--cream);
  }
  .card {
    position: relative;
    width: 630px; height: 360px;
    border-radius: 22px;
    background: radial-gradient(ellipse at 50% 50%, var(--card) 55%, var(--card-deep) 100%);
    overflow: hidden;
  }
  .card__frame {
    position: absolute; inset: 16px;
    border: 3px solid var(--ink);
    pointer-events: none;
  }
  .art { position: absolute; }
  .art--hat {
    left: 26px; bottom: 26px; width: 120px; height: 90px;
    border-radius: 50% 50% 40% 40%;
    background: radial-gradient(ellipse at 50% 40%, var(--leather), var(--card-deep) 75%);
  }
  .art--boots {
    right: 16px; top: 16px; width: 110px; height: 130px;
    border-radius: 26px 26px 16px 34px;
    background: linear-gradient(160deg, var(--tan-light), var(--leather) 60%, var(--ink));
  }
  .art--boots-small {
    right: 22px; bottom: 24px; width: 50px; height: 70px;
    border-radius: 14px 14px 8px 18px;
    background: linear-gradient(160deg, var(--tan-light), var(--leather) 60%, var(--ink));
  }
  /* Front */
  .front__text {
    position: absolute; left: 150px; top: 38px; width: 350px;
    text-align: center;
  }
  .brand {
    font-family: "Lobster", cursive; font-weight: 400;
    font-size: 38px; line-height: 1; white-space: nowrap;
  }
  .with {
    display: flex; align-items: center; gap: 8px;
    font-family: "Montserrat", sans-serif; font-weight: 500;
    font-size: 13px; letter-spacing: 2px; margin: 8px 0 2px;
  }
  .with::before, .with::after { content: ""; flex: 1; height: 1px; background: var(--cream); opacity: .7; }
  .host {
    font-family: "Alfa Slab One", serif;
    font-size: 80px; line-height: 1; letter-spacing: 2px;
  }
  .tagline {
    font-family: "Lora", serif; font-style: italic;
    font-size: 19px; line-height: 1.2; margin-top: 8px;
  }
  .phone {
    display: flex; align-items: center; justify-content: center; gap: 10px;
    font-family: "Oswald", sans-serif; font-weight: 600;
    font-size: 44px; line-height: 1; margin-top: 10px; white-space: nowrap;
  }
  .phone svg { width: 34px; height: 34px; flex: none; }
  /* Back */
  .headshot {
    position: absolute; left: 50px; top: 62px; width: 200px; height: 200px;
    border-radius: 28px;
    background: linear-gradient(180deg, var(--tan) 0%, var(--tan-light) 100%);
  }
  .owner {
    position: absolute; left: 50px; top: 274px; width: 200px; text-align: center;
    font-family: "Lobster", cursive; font-weight: 400; font-size: 34px; white-space: nowrap;
  }
  .back__info { position: absolute; left: 276px; top: 58px; width: 272px; }
  .quote {
    font-family: "Montserrat", sans-serif; line-height: 1;
    padding-bottom: 10px; border-bottom: 1px solid var(--cream);
  }
  .quote__lead { display: block; font-weight: 600; font-size: 21px; letter-spacing: 1px; }
  .quote__main { display: block; font-weight: 800; font-size: 31px; }
  .styles {
    display: grid; grid-template-columns: 1fr 1fr; gap: 2px 12px;
    list-style: none; padding: 12px 0 10px;
    font-family: "Montserrat", sans-serif; font-weight: 500; font-size: 17px;
    border-bottom: 1px solid var(--cream);
  }
  .styles li { display: flex; align-items: center; gap: 7px; white-space: nowrap; }
  .styles svg { width: 16px; height: 16px; flex: none; }
  .back__info .phone { justify-content: flex-start; font-size: 44px; margin-top: 12px; }
</style>
</head>
<body>

<section class="card card--front">
  <div class="card__frame"></div>
  <div class="art art--hat" role="img" aria-label="Illustration of a cowboy hat"></div>
  <div class="art art--boots" role="img" aria-label="Illustration of cowboy boots with a lasso"></div>
  <div class="front__text">
    <h1 class="brand">Lanternfield Dance</h1>
    <p class="with">WITH</p>
    <p class="host">MARK</p>
    <p class="tagline">Take The Challenge<br>Experience The Growth</p>
    <p class="phone">
      <svg viewBox="0 0 24 24" fill="none" stroke="currentColor" stroke-width="1.8" stroke-linejoin="round"><path d="M5 4h4l2 5-2.5 1.5a11 11 0 0 0 5 5L15 13l5 2v4a2 2 0 0 1-2 2A16 16 0 0 1 3 6a2 2 0 0 1 2-2z"/></svg>
      210-574-2318
    </p>
  </div>
</section>

<section class="card card--back">
  <div class="card__frame"></div>
  <div class="headshot" role="img" aria-label="Space for a head shot"></div>
  <p class="owner">Mark Delby</p>
  <div class="art art--boots-small" role="img" aria-label="Illustration of cowboy boots"></div>
  <div class="back__info">
    <h2 class="quote">
      <span class="quote__lead">EXPERIENCE IS THE</span>
      <span class="quote__main">BEST TEACHER</span>
    </h2>
    <ul class="styles">
      <li><svg viewBox="0 0 16 16" fill="none" stroke="currentColor" stroke-width="1.8"><rect x="1.5" y="1.5" width="13" height="13"/><path d="M4 8l3 3 5-6"/></svg>Two Step</li>
      <li><svg viewBox="0 0 16 16" fill="none" stroke="currentColor" stroke-width="1.8"><rect x="1.5" y="1.5" width="13" height="13"/><path d="M4 8l3 3 5-6"/></svg>Cha-Cha</li>
      <li><svg viewBox="0 0 16 16" fill="none" stroke="currentColor" stroke-width="1.8"><rect x="1.5" y="1.5" width="13" height="13"/><path d="M4 8l3 3 5-6"/></svg>Waltz</li>
      <li><svg viewBox="0 0 16 16" fill="none" stroke="currentColor" stroke-width="1.8"><rect x="1.5" y="1.5" width="13" height="13"/><path d="M4 8l3 3 5-6"/></svg>West Coast</li>
      <li><svg viewBox="0 0 16 16" fill="none" stroke="currentColor" stroke-width="1.8"><rect x="1.5" y="1.5" width="13" height="13"/><path d="M4 8l3 3 5-6"/></svg>Triple Two</li>
      <li><svg viewBox="0 0 16 16" fill="none" stroke="currentColor" stroke-width="1.8"><rect x="1.5" y="1.5" width="13" height="13"/><path d="M4 8l3 3 5-6"/></svg>East Cost</li>
      <li><svg viewBox="0 0 16 16" fill="none" stroke="currentColor" stroke-width="1.8"><rect x="1.5" y="1.5" width="13" height="13"/><path d="M4 8l3 3 5-6"/></svg>Polka</li>
      <li><svg viewBox="0 0 16 16" fill="none" stroke="currentColor" stroke-width="1.8"><rect x="1.5" y="1.5" width="13" height="13"/><path d="M4 8l3 3 5-6"/></svg>NightClub</li>
    </ul>
    <p class="phone">
      <svg viewBox="0 0 24 24" fill="none" stroke="currentColor" stroke-width="1.8" stroke-linejoin="round"><path d="M5 4h4l2 5-2.5 1.5a11 11 0 0 0 5 5L15 13l5 2v4a2 2 0 0 1-2 2A16 16 0 0 1 3 6a2 2 0 0 1 2-2z"/></svg>
      210-574-2318
    </p>
  </div>
</section>

</body>
</html>
```